Marketing Brochure - Conjunction event

We need a brochure for clients/conjunction real estate agents to view the type of projects VARO531 have available.
As a guideline of our requirements, please refer to our company profile. As you can see it is a simple elegant professional image we are after.
We are a Real Estate company specialise in off the plans project marketing. We have sale teams to sell the projects/ residential properties but also conjunction with other real estate agents. This is the first time we decided to use QuillMarket to design our brochure. If pleasing results, ongoing we will have many more design projects to do.

Target Market(s)

Clients / real estate agents

Industry/Entity Type

Real Estate

Font styles to use
Sans Serif

Colors
ffffff
ef484e

Requirements
Must have
• All the details in the documents, Encourage creative designs.
• Company logo and the black banner as seen on company profile brochure
Nice to have
• similar to our company profile brochure( file attached)
Should not have
• Funky or too loud type image

```html
<!DOCTYPE html>
<html lang="en">
<head>
<meta charset="utf-8">
<title>VARO531 Conjunction Agent Event Brochure</title>
<link rel="stylesheet" href="https://fonts.googleapis.com/css2?family=Open+Sans:wght@400;600;700&family=Libre+Baskerville:wght@400;700&display=swap">
<style>
  :root{
    --red:#ef484e;
    --white:#ffffff;
    --stage:#2b2b2b;
    --panel-grey:#ddd5d7;
    --logo-grey:#8b8a8a;
    --banner-black:#1e1d1e;
    --text:#4a4a4a;
    --text-dark:#2e2e2e;
    --band-pink:rgba(239,120,110,.5);
  }
  *{box-sizing:border-box;margin:0;padding:0}
  html,body{width:900px;height:1200px;overflow:hidden;background:var(--stage);font-family:"Open Sans",Arial,sans-serif;color:var(--text)}
  .canvas{position:relative;width:900px;height:1200px}
  .page{position:absolute;left:78px;width:762px;height:588px;background:var(--white);overflow:hidden}
  .page--cover{top:8px}
  .page--inside{top:604px}
  .block{position:absolute}
  .photo{position:absolute}
  /* cover */
  .intro{left:9px;top:7px;width:368px;height:337px;background:var(--panel-grey)}
  .intro__title{position:absolute;top:22px;width:100%;text-align:center;font-family:"Libre Baskerville",Georgia,serif;font-weight:400;font-size:18px;color:#555}
  .address{position:absolute;width:100%;text-align:center;color:#6a6a6a}
  .intro .address{top:278px;font-size:14px;line-height:21px}
  .second{left:9px;top:459px;width:368px;height:118px;background:linear-gradient(#f6d4d0,#f1c1bc)}
  .second .address{top:5px;font-size:12px;line-height:16px;color:#444}
  .brand{position:absolute;display:flex;align-items:center;gap:6px;font-weight:700;letter-spacing:1px}
  .second .brand{left:120px;top:56px;font-size:22px;color:var(--red)}
  .brand__mark{width:13px;height:13px;background:currentColor;border-radius:50%}
  .event{left:381px;top:490px;width:237px;height:87px;background:var(--red);color:var(--white);font-weight:700;font-size:20px;line-height:29px;text-align:center;padding-top:15px}
  .logo-tile{left:624px;top:7px;width:127px;height:92px;background:var(--logo-grey)}
  .logo-tile .brand{left:0;right:0;top:35px;justify-content:center;font-size:17px;color:var(--white);letter-spacing:.5px}
  .logo-tile .brand__mark{width:11px;height:11px}
  .banner{left:624px;top:107px;width:127px;height:470px;background:radial-gradient(ellipse at 50% 40%,#2c2b2c 0%,var(--banner-black) 70%)}
  /* inside */
  .inside__body{position:absolute;left:10px;top:10px;width:742px;height:576px;background:linear-gradient(180deg,#ececec,#d6d6d6)}
  .band{position:absolute;top:0;width:94px;height:571px;background:var(--band-pink)}
  .band--left{left:15px}
  .band--right{left:627px}
  .tag{position:absolute;background:linear-gradient(#ffffff,#d9d9d9);font-weight:700;font-size:13px;color:var(--text-dark);padding:0 6px;box-shadow:0 1px 2px rgba(0,0,0,.25);white-space:nowrap}
  .tag::after{content:"";position:absolute;bottom:-7px;border-style:solid}
  .tag--l::after{left:0;border-width:0 7px 7px 0;border-color:transparent var(--red) transparent transparent}
  .tag--r::after{right:0;border-width:0 0 7px 7px;border-color:transparent transparent transparent var(--red)}
  .list{position:absolute;font-size:12.6px;line-height:16.2px;color:#3a3a3a;list-style:none;letter-spacing:-.25px}
  .list li{position:relative;padding-left:13px}
  .list li::before{content:"";position:absolute;left:1px;top:6px;width:5px;height:5px;border-radius:50%;background:#666}
  .credits{position:absolute;font-size:12.5px;line-height:16px;color:#3a3a3a}
  .credits dt{font-weight:700}
</style>
</head>
<body>
<div class="canvas">

  <section class="page page--cover">
    <div class="block intro">
      <h1 class="intro__title">Stage II - Launch Next Week</h1>
      <div class="photo" role="img" aria-label="Rendering of a modern mid-rise apartment building with yellow trim under a blue sky" style="left:17px;top:62px;width:337px;height:195px;background:radial-gradient(ellipse at 60% 55%,rgba(240,236,220,.85) 0%,rgba(240,236,220,0) 45%),radial-gradient(ellipse at 8% 50%,rgba(70,110,60,.8) 0%,rgba(70,110,60,0) 30%),linear-gradient(180deg,#4f86c9 0%,#a9c8e8 32%,#d9d6c8 52%,#6d6a63 72%,#3b3f35 88%,#4d6b3c 100%)"></div>
      <p class="address">Address: 88-102 Larkspur Ridge Drive,<br>Hollowvale NSW 2160</p>
    </div>
    <div class="photo" role="img" aria-label="Rendering of a tall apartment tower at street level" style="left:9px;top:349px;width:180px;height:106px;background:radial-gradient(ellipse at 45% 55%,rgba(214,200,170,.9) 0%,rgba(214,200,170,0) 45%),linear-gradient(180deg,#4d7fbf 0%,#a8c3e0 35%,#b8ad94 60%,#5e5a4c 85%,#3f4a33 100%)"></div>
    <div class="photo" role="img" aria-label="Rendering of an apartment complex at sunset" style="left:193px;top:349px;width:184px;height:106px;background:radial-gradient(ellipse at 60% 50%,rgba(222,170,120,.9) 0%,rgba(222,170,120,0) 50%),linear-gradient(180deg,#7f98bf 0%,#c9b49a 40%,#a97e5a 65%,#5a4636 88%,#3b3a2c 100%)"></div>
    <div class="block second">
      <p class="address">Address: 210-236 Coastline Highway,<br>Elmbrook NSW 2218</p>
      <div class="brand"><span class="brand__mark"></span>VARO531</div>
    </div>
    <div class="photo" role="img" aria-label="Rooftop terrace with pool and city skyline at dusk" style="left:381px;top:7px;width:237px;height:238px;background:radial-gradient(ellipse at 80% 75%,rgba(70,160,220,.85) 0%,rgba(70,160,220,0) 30%),radial-gradient(ellipse at 45% 55%,rgba(230,200,160,.55) 0%,rgba(230,200,160,0) 35%),linear-gradient(180deg,#3f4a8a 0%,#7b74a8 28%,#b49aa4 45%,#4a4350 60%,#6b5a4c 80%,#3d3530 100%)"></div>
    <div class="photo" role="img" aria-label="Black and white view of apartment blocks with a blossoming tree" style="left:381px;top:252px;width:237px;height:232px;background:radial-gradient(ellipse at 30% 40%,rgba(245,245,245,.95) 0%,rgba(245,245,245,0) 30%),radial-gradient(ellipse at 70% 35%,rgba(225,225,225,.8) 0%,rgba(225,225,225,0) 28%),linear-gradient(180deg,#6a6a6a 0%,#a8a8a8 30%,#8a8a8a 55%,#3c3c3c 75%,#9a9a9a 100%)"></div>
    <div class="block event">Conjunction Agent<br>Event</div>
    <div class="block logo-tile"><div class="brand"><span class="brand__mark"></span>VARO531</div></div>
    <div class="block banner"></div>
  </section>

  <section class="page page--inside">
    <div class="inside__body">
      <div class="photo" role="img" aria-label="Rendering of white and grey apartment buildings" style="left:0;top:0;width:370px;height:196px;background:radial-gradient(ellipse at 55% 45%,rgba(245,245,245,.9) 0%,rgba(245,245,245,0) 40%),radial-gradient(ellipse at 20% 60%,rgba(150,90,80,.6) 0%,rgba(150,90,80,0) 30%),linear-gradient(180deg,#9fb3c9 0%,#d6dce3 35%,#8e949a 65%,#4e5a48 100%)"></div>
      <div class="photo" role="img" aria-label="Apartment tower and streetscape at dusk" style="left:370px;top:0;width:372px;height:196px;background:radial-gradient(ellipse at 30% 40%,rgba(200,190,170,.85) 0%,rgba(200,190,170,0) 40%),radial-gradient(ellipse at 75% 80%,rgba(230,170,90,.6) 0%,rgba(230,170,90,0) 30%),linear-gradient(180deg,#7d8fa8 0%,#b4b2a8 40%,#6e6455 70%,#3c3a30 100%)"></div>
      <svg class="block" style="left:0;top:90px" width="742" height="140" viewBox="0 0 742 140">
        <path d="M0 52 C110 10 170 -10 240 12 C300 30 340 60 370 90 C400 60 440 20 500 8 C580 -6 660 30 742 52 L742 140 L0 140 Z" fill="var(--red)"/>
        <path d="M0 72 C110 30 170 10 240 30 C300 48 340 80 370 110 C400 80 440 40 500 28 C580 14 660 50 742 72 L742 140 L0 140 Z" fill="#ececec"/>
      </svg>
      <div class="band band--left"></div>
      <div class="band band--right"></div>
    </div>

    <div class="tag tag--l" style="left:17px;top:214px;height:22px;line-height:22px">Feature Include</div>
    <ul class="list" style="left:128px;top:220px;width:262px">
      <li>Mix of spacious 1, 2 &amp; 3 bedroom<br>apartments</li>
      <li>Sunny north-east facing</li>
      <li>Only 15 min Sydney CBD</li>
      <li>Walk to Eastwick &amp; Maple Hill train<br>stations</li>
      <li>Close to transport, parks, shopping<br>amenities and highly reputable schools</li>
      <li>High quality finishes with modern fittings</li>
      <li>Design by award winning architects<br>Arcline Studio</li>
    </ul>

    <div class="tag tag--l" style="left:17px;top:414px;width:110px;line-height:16px;padding:1px 14px;white-space:normal">Deposit Requirement</div>
    <ul class="list" style="left:128px;top:422px;width:250px">
      <li>10% deposit (Cash Deposit, Bank<br>Guarantee)</li>
      <li>Council Rates: $238 Per quarter</li>
      <li>Water Rates: $175 per quarter</li>
    </ul>

    <dl class="credits" style="left:128px;top:493px"><dt>Developer</dt><dd>Northgate Pty Ltd</dd></dl>
    <dl class="credits" style="left:275px;top:493px"><dt>Architect</dt><dd>Arcline Studio</dd></dl>
    <dl class="credits" style="left:185px;top:537px;text-align:center"><dt>Builder</dt><dd>Brightstone Construction</dd></dl>

    <ul class="list" style="left:390px;top:224px;width:245px">
      <li>Mix of spacious 1, 2 &amp; 3bedroom<br>apartments</li>
      <li>Just 6 min to Brisbane CBD via<br>HarbourLink T4</li>
      <li>7 min drive to international airports</li>
      <li>Quality schools – St Clement<br>College and Rivergum State Primary<br>School Train – 7 stops to CBD 2 major<br>shopping centres, child care facilities,<br>parks, the Greenfield and Kestrel Park<br>Racecourses</li>
      <li>Precinct facilities - Extensive new retail<br>plazas including bars, cafes and indoor<br>and outdoor dining at Solace; 2,000m2<br>“Pulse Well” super club at Solace; Private<br>resident only lounge and media room</li>
    </ul>
    <ul class="list" style="left:390px;top:520px;width:230px">
      <li>10% deposit (Cash Deposit, Bank<br>Guarantee)</li>
    </ul>

    <div class="tag tag--r" style="left:629px;top:214px;height:22px;line-height:22px">Feature Include</div>
    <div class="tag tag--r" style="left:637px;top:503px;width:104px;line-height:16px;padding:1px 8px;white-space:normal">Deposit Requirement</div>
  </section>

</div>
</body>
</html>
```